QTR Newsletter

QTR provides mortgage processing outsource services to Mortgage Lenders in Australia and New Zealand. The company employs approximately 300 staff based in offices in Sydney, Melbourne, Brisbane, Adelaide and Perth in Australia and Auckland, New Zealand.
The company acquired a similar and much larger business in 2012 which is being integrated into the one business.
The objectives of a newsletter are to:
- Support the development of the company culture
- Develp a sense of "one team"
- Provide a communication forum for management and staff
I am seeking design options for the newsletter. We will develop/include specific content which will likley evolve over time.
A copy of the company brand gudelines and logo is attached for reference. Our website is currently going through a redesign. Additional information can be provided on request.

Target Market(s)

The target market for the newsletter is staff. This is a diverse group in terms of locations, age, gender, occupations etc.

Industry/Entity Type

Communication

Requirements
Must have
• Information to be included in the newsletter should include:
- Business results (activity, volumes, performance to budget)
- Client news section (recent developments, client profiling etc)
- New initiatives (update on key projects and new business initiatives, initiatives roadmap)
- Office news (news section for each office including new employees, team profile of the month, report on social events)
- CEO report

```html
<!DOCTYPE html>
<html lang="en">
<head>
<meta charset="utf-8">
<title>QTR Newsletter</title>
<link href="https://fonts.googleapis.com/css2?family=Cinzel:wght@400;600;700&family=Jost:wght@400;500;700&display=swap" rel="stylesheet">
<style>
  :root {
    --page-bg: #ffffff;
    --frame: #666666;
    --sheet: #6699cc;
    --navy: #0b2c62;
    --navy-deep: #061d45;
    --ink: #000000;
    --white: #ffffff;
    --heading-light: #a8ccf2;
    --link-light: #8fb4e0;
  }
  * { margin: 0; padding: 0; box-sizing: border-box; }
  html, body { width: 1200px; height: 1000px; overflow: hidden; background: var(--page-bg); }
  body { position: relative; font-family: "Jost", sans-serif; color: var(--white); }

  .frame { position: absolute; left: 273px; top: 28px; width: 672px; height: 950px; background: var(--frame); }
  .sheet { position: absolute; left: 285px; top: 40px; width: 647px; height: 938px; background: var(--sheet); }

  .masthead { position: absolute; left: 285px; top: 40px; width: 647px; height: 150px;
    background: linear-gradient(90deg, #04204f 0%, #0a3a7f 45%, #2a66b8 75%, #3b78c8 100%); overflow: hidden; }
  .masthead-photo { position: absolute; left: 290px; top: 0; width: 357px; height: 150px;
    background: linear-gradient(90deg, rgba(40,90,170,0) 0%, rgba(60,115,200,0.7) 40%, rgba(90,140,215,0.85) 100%); }
  .masthead-rule { position: absolute; left: 285px; top: 190px; width: 647px; height: 6px; background: var(--ink); }
  .brand-name { position: absolute; left: 22px; top: 8px; font-family: "Cinzel", serif; font-weight: 400;
    font-size: 98px; letter-spacing: 2px; line-height: 1; color: var(--white); }
  .tagline { position: absolute; left: 37px; top: 116px; font-size: 18px; color: var(--white); }
  .office { position: absolute; top: 90px; text-align: center; width: 130px; }
  .office-city { font-family: "Cinzel", serif; font-weight: 600; font-size: 17px; letter-spacing: 1px; }
  .office-phone { font-size: 16px; margin-top: 5px; }
  .office-auckland { left: 298px; }
  .office-melbourne { left: 455px; }

  .section-title { position: absolute; font-family: "Cinzel", serif; font-weight: 700; font-size: 22px; color: var(--white); letter-spacing: 0.5px; }
  .body-copy { position: absolute; font-size: 13.6px; line-height: 16.2px; text-align: justify; hyphens: auto; }
  .read-more { color: var(--ink); }

  .title-results { left: 299px; top: 207px; }
  .copy-results { left: 299px; top: 250px; width: 613px; }

  .feature-photo { position: absolute; left: 297px; top: 377px; width: 386px; height: 255px; border: 2px solid var(--ink);
    background: linear-gradient(135deg, #e9eef2 0%, #c9d3dc 40%, #6c7f94 70%, #2c3440 100%); }

  .title-initiatives { left: 299px; top: 647px; }
  .copy-initiatives { left: 299px; top: 689px; width: 385px; }

  .sidebar { position: absolute; left: 698px; top: 377px; width: 219px; height: 482px; background: var(--navy); border: 1.5px solid var(--ink); }
  .sidebar-title { position: absolute; left: 14px; width: 191px; height: 26px; background: var(--ink);
    font-family: "Cinzel", serif; font-weight: 700; font-size: 19px; line-height: 27px; text-align: center; color: var(--heading-light); }
  .sidebar-copy { position: absolute; left: 14px; width: 192px; font-size: 13.4px; line-height: 16.3px; text-align: justify; }
  .sidebar-copy .more { color: var(--link-light); }

  .footer { position: absolute; left: 285px; top: 870px; width: 647px; text-align: center; color: var(--ink); }
  .follow { font-size: 7px; font-weight: 500; }
  .social { display: flex; justify-content: center; gap: 5px; margin-top: 9px; }
  .social span { width: 24px; height: 24px; background: var(--navy); border-radius: 5px; display: block; }
  .footer-links { font-size: 7px; font-weight: 500; margin-top: 16px; letter-spacing: 0.2px; }
  .footer-note { font-size: 6.6px; line-height: 11px; margin-top: 1px; }
  .footer-note b { font-weight: 700; }
</style>
</head>
<body>
  <div class="frame"></div>
  <div class="sheet"></div>

  <header class="masthead">
    <div class="masthead-photo" role="img" aria-label="Photo of a business team meeting around a table"></div>
    <div class="brand-name">QTR</div>
    <div class="tagline">Global reach. Local touch.</div>
    <div class="office office-auckland"><div class="office-city">AUCKLAND</div><div class="office-phone">+64 9 555 0142</div></div>
    <div class="office office-melbourne"><div class="office-city">MELBOURNE</div><div class="office-phone">+61 3 5550 1187</div></div>
  </header>
  <div class="masthead-rule"></div>

  <h2 class="section-title title-results">Business Results</h2>
  <p class="body-copy copy-results">Lorem ipsum dolor sit amet, consectetur adipisicing elit, sed do eiusmod tempor incididunt ut labore et dolore magna aliqua. Ut enim ad minim veniam, quis nostrud exercitation ullamco laboris nisi ut aliquip ex ea commodo consequat. Duis aute irure dolor in reprehenderit in voluptate velit esse cillum dolore eu fugiat nulla pariatur. Excepteur sint occaecat cupidatat non proident, sunt in culpa qui officia deserunt mollit anim id est laborum."Lorem ipsum dolor sit amet, consectetur adipisicing elit, sed do eiusmod tempor incididunt ut labore et dolore magna&nbsp; aliqua. <span class="read-more">&gt; Read more</span></p>

  <div class="feature-photo" role="img" aria-label="Photo of an adviser reviewing a document with a smiling couple"></div>

  <h2 class="section-title title-initiatives">New Initiatives</h2>
  <p class="body-copy copy-initiatives">Lorem ipsum dolor sit amet, consectetur adipisicing elit, sed do eiusmod tempor incididunt ut labore et dolore magna aliqua. Ut enim ad minim veniam, quis nostrud exercitation ullamco laboris nisi ut aliquip ex ea commodo consequat. Duis aute irure dolor in reprehenderit in voluptate velit esse cillum dolore eu fugiat nulla pariatur. Excepteur sint occaecat cupidatat non proident, sunt in culpa qui officia deserunt mollit anim id est laborum."Lorem ipsum dolor sit amet, consectetur adipisicing elit, sed do eiusmod tempor incididunt ut labore et dolore magna&nbsp; aliqua. <span class="read-more">&gt; Read more</span></p>

  <aside class="sidebar">
    <h3 class="sidebar-title" style="top:14px;">Office News</h3>
    <p class="sidebar-copy" style="top:54px;">Lorem ipsum dolor sit amet, consectetur adipisicing elit, sed do eiusmod tempor incididunt ut labore et dolore magna aliqua. Ut smod tempor incididunt ut labore et dolore magna&nbsp; aliqua.<br>&gt; <span class="more">Read more</span></p>
    <h3 class="sidebar-title" style="top:187px;">Client News</h3>
    <p class="sidebar-copy" style="top:227px;">Lorem ipsum dolor sit amet, consectetur adipisicing elit, sed do eiusmod tempor incididunt ut labore et dolore magna aliqua. Ut smod tempor incididunt ut labore et dolore magna&nbsp; aliqua.<br>&gt; <span class="more">Read more</span></p>
    <h3 class="sidebar-title" style="top:357px;">CEO Report</h3>
    <p class="sidebar-copy" style="top:397px;">Lorem ipsum dolor sit amet, consectetur adipisicing elit, sed do eiusmod tempor incididunt ut<br>&gt; <span class="more">Read more</span></p>
  </aside>

  <footer class="footer">
    <div class="follow">Follow Us On</div>
    <div class="social"><span></span><span></span><span></span><span></span></div>
    <div class="footer-links">SHARE THIS NEWSLETTER | FORWARD TO A FRIEND &nbsp;| PRIVACY POLICY</div>
    <div class="footer-note">This email was sent to you because you are subscribed to QTR Mail,<br>the periodic newsletter of the QTR Marketplaces. To Unsubscribe from this List, <b>Click Here</b></div>
  </footer>
</body>
</html>
```